Medical equipment business looking for professional, unique business card

We need a business card design for a durable medical equipment company. We are small but would like our cards to express that we are much bigger. We focus on braces (back, knee, wrist, etc) but also do crutches, rollators, wheelchairs- basically medical equipment that gets you going and back in Action. Our colors are blue and green and our logo has an arrow and use of a "spine". We'd like to express professionalism while being unique.

Industry/Entity Type

Medical Equipment

Contact Information for Business Card

Professional feel but unique. Memorable.

Font styles to use
Serif
Sans Serif
Other font styles liked:
• verdana

Requirements
Must have
• card holders cell#, business phone#, fax#, email, website address, business address, logo
Nice to have
• use of medical/healthcare related descriptive words, items, look
Should not have
• the wrong colors or cartoon characters.

```html
<!DOCTYPE html>
<html lang="en">
<head>
<meta charset="utf-8">
<title>Stride Medical – Business Card</title>
<link rel="stylesheet" href="https://fonts.googleapis.com/css2?family=Open+Sans:wght@400;600&display=swap">
<style>
  :root {
    --stage: #3a3a3a;
    --lime: #8dd13a;
    --navy: #0f5585;
    --navy-deep: #0c4a75;
    --sky: #2aa3dc;
    --green: #8cc63f;
    --ink: #1c4f86;
    --white: #ffffff;
  }
  * { margin: 0; padding: 0; box-sizing: border-box; }
  html, body { width: 1200px; height: 950px; overflow: hidden; }
  body {
    background: var(--stage);
    font-family: "Open Sans", Verdana, sans-serif;
    position: relative;
  }
  .card {
    position: absolute;
    left: 250px;
    width: 700px;
    height: 400px;
    overflow: hidden;
  }
  .card-front { top: 50px; background: var(--lime); }
  .card-back { top: 500px; background: var(--white); }

  .brand { position: absolute; display: flex; align-items: center; gap: 12px; }
  .brand-dot { width: 22px; height: 22px; border-radius: 50%; background: var(--ink); }
  .brand-name { font-size: 44px; font-weight: 600; color: var(--ink); line-height: 1; }
  .brand-tagline { position: absolute; font-size: 17px; font-weight: 600; color: var(--ink); }

  .card-front .brand { left: 170px; top: 140px; }
  .card-front .brand-tagline { left: 204px; top: 192px; }
  .website {
    position: absolute; left: 0; right: 0; top: 300px;
    text-align: center; font-size: 15px; letter-spacing: 0.45em; color: var(--ink);
  }

  .card-back .brand { left: 150px; top: 95px; }
  .card-back .brand-name { color: var(--navy); }
  .card-back .brand-dot { background: var(--navy); }
  .card-back .brand-tagline { left: 184px; top: 147px; color: var(--sky); }

  .wave { position: absolute; inset: 0; }

  .contacts {
    position: absolute; right: 26px; top: 175px;
    list-style: none; text-align: right; color: var(--white); font-size: 16px;
  }
  .contacts li { display: flex; justify-content: flex-end; align-items: center; gap: 10px; height: 26px; }
  .contacts svg { width: 16px; height: 16px; fill: var(--white); }

  .holder { position: absolute; left: 40px; top: 290px; color: var(--white); }
  .holder-name { font-size: 22px; font-weight: 600; color: var(--green); }
  .holder-title { font-size: 17px; margin-bottom: 6px; }
  .holder-address { font-size: 16px; line-height: 1.35; font-style: normal; }
</style>
</head>
<body>

<section class="card card-front">
  <div class="brand">
    <span class="brand-dot"></span>
    <span class="brand-name">Stride Medical</span>
  </div>
  <p class="brand-tagline">Durable Medical Equipment</p>
  <p class="website">www.stridemedical.com</p>
</section>

<section class="card card-back">
  <svg class="wave" viewBox="0 0 700 400" preserveAspectRatio="none">
    <path d="M0,262 C170,238 320,316 455,196 C555,106 640,124 700,112 L700,400 L0,400 Z" fill="var(--sky)"/>
    <path d="M0,276 C170,252 320,330 460,210 C560,122 640,138 700,126 L700,400 L0,400 Z" fill="var(--navy)"/>
    <path d="M380,246 C420,220 440,196 470,172 C560,98 640,104 700,92" fill="none" stroke="var(--green)" stroke-width="5"/>
  </svg>

  <div class="brand">
    <span class="brand-dot"></span>
    <span class="brand-name">Stride Medical</span>
  </div>
  <p class="brand-tagline">Durable Medical Equipment</p>

  <ul class="contacts">
    <li>555 0142 7731
      <svg viewBox="0 0 16 16"><path d="M3 1h3l1.5 4-2 1.5a9 9 0 0 0 4 4L11 8.5l4 1.5v3a2 2 0 0 1-2 2A12 12 0 0 1 1 3a2 2 0 0 1 2-2z"/></svg></li>
    <li>555 0187 4409
      <svg viewBox="0 0 16 16"><path d="M4 0h8a1 1 0 0 1 1 1v14a1 1 0 0 1-1 1H4a1 1 0 0 1-1-1V1a1 1 0 0 1 1-1zm1 2v10h6V2z"/></svg></li>
    <li>555 0163 2218
      <svg viewBox="0 0 16 16"><path d="M4 0h7v4H4zM1 5h14v8h-3v3H4v-3H1zm4 6v3h6v-3z"/></svg></li>
    <li>daniel@stridemedical.com
      <svg viewBox="0 0 16 16"><path d="M0 3h16v10H0zm1.5 1.2L8 9l6.5-4.8V4H1.5z"/></svg></li>
  </ul>

  <div class="holder">
    <p class="holder-name">Daniel Reyes</p>
    <p class="holder-title">President</p>
    <address class="holder-address">1420 Harbor Point Road<br>Lakeview, NY 10000</address>
  </div>
</section>

</body>
</html>
```